Business Card Design for Varnok Facility Services

We are looking for a Business Card Design for the Company "Varnok Facility Services."
Front side:
- Company Logo (small)
- Company Name, address, pohone, website and personal data.
- white background, for text e.g. company colors (blue or green like in the logo)
Please use following data:
Company data:
Varnok Facility Services Tulbrecht
Kirchmattweg 12
6331 Cham
www.varnok-fs.ch
Person data:
Ruben Tulbrecht
Geschäftsführer
+41 76 519 84 60
info@varnok-fs.ch
Back side:
could be colored in blue or green
please use a big logo sing and some smaller icons to say what is all beeing offered in facility services, like cleaning, maintenance cleaning
industrial cleaning, caretaking, gardening, disposal. There is no need for everyone of the icons if there are similar or an icon is standing for more of them.
Cleaning Service
colors to use:
blue: HEX 246BB0
green: HEX 52B33E

```html
<!DOCTYPE html>
<html lang="de">
<head>
<meta charset="utf-8">
<title>Varnok Facility Services – Visitenkarte</title>
<link rel="stylesheet" href="https://fonts.googleapis.com/css2?family=Source+Sans+3:wght@400;600;700&display=swap">
<style>
  :root {
    --brand-green: #52B33E;
    --brand-blue: #246BB0;
    --paper: #ffffff;
    --backdrop: #ececec;
    --font-text: "Source Sans 3", sans-serif;
  }
  * { margin: 0; padding: 0; box-sizing: border-box; }
  html, body {
    width: 1200px; height: 800px; overflow: hidden;
    background: var(--backdrop);
    font-family: var(--font-text);
  }
  .stage { position: relative; width: 1200px; height: 800px; }
  .card {
    position: absolute; top: 280px;
    width: 420px; height: 240px; overflow: hidden;
  }
  /* Back side */
  .card--back { left: 142px; background: var(--brand-green); color: var(--paper); text-align: center; }
  .brand-name {
    position: absolute; left: 0; right: 0; top: 96px;
    font-size: 24px; font-weight: 600; letter-spacing: 0.5px; line-height: 1;
  }
  .services {
    position: absolute; left: 0; right: 0; top: 171px;
    font-size: 15.5px; font-weight: 400; line-height: 18px;
  }
  /* Front side */
  .card--front { left: 639px; background: var(--paper); }
  .card-swoosh { position: absolute; inset: 0; width: 100%; height: 100%; }
  .contact { position: absolute; left: 142px; top: 44px; }
  .person-name {
    font-size: 17px; font-weight: 700; color: var(--brand-blue);
    letter-spacing: 0.3px; line-height: 19px;
  }
  .person-role { font-size: 14.5px; color: var(--brand-green); line-height: 18px; }
  .contact-list { list-style: none; margin-top: 14px; }
  .contact-item {
    position: relative; padding-left: 23px;
    font-size: 15px; line-height: 20px; color: var(--brand-blue);
  }
  .contact-item + .contact-item { margin-top: 0; }
  .contact-item--gap { margin-top: 5px !important; }
  .contact-item--green { color: var(--brand-green); }
  .contact-icon { position: absolute; left: 0; top: 4px; width: 12px; height: 12px; }
</style>
</head>
<body>
<main class="stage">

  <section class="card card--back" aria-label="Rückseite">
    <p class="brand-name">Varnok Facility Services</p>
    <p class="services">Cleaning . Maintenance Cleaning<br>Industrial Cleaning . Caretaking . Gardening . Disposal</p>
  </section>

  <section class="card card--front" aria-label="Vorderseite">
    <svg class="card-swoosh" viewBox="0 0 420 240" aria-hidden="true">
      <path d="M0 0 H129 Q74 120 118 240 H0 Z" fill="var(--brand-green)"/>
      <path d="M141 0 Q86 120 130 240" fill="none" stroke="var(--brand-blue)" stroke-width="8"/>
    </svg>

    <div class="contact">
      <p class="person-name">RUBEN TULBRECHT</p>
      <p class="person-role">Geschäftsführer</p>
      <ul class="contact-list">
        <li class="contact-item">
          <svg class="contact-icon" viewBox="0 0 12 12" aria-hidden="true"><rect width="12" height="12" fill="var(--brand-green)"/><path d="M6 2.2a2.3 2.3 0 0 1 2.3 2.3C8.3 6.2 6 8.6 6 8.6S3.7 6.2 3.7 4.5A2.3 2.3 0 0 1 6 2.2z" fill="#fff"/><circle cx="6" cy="4.5" r="0.9" fill="var(--brand-green)"/><rect x="2.5" y="9.2" width="7" height="1" fill="#fff"/></svg>
          Varnok Facility Services Tulbrecht<br>Kirchmattweg 12, 6331 Cham
        </li>
        <li class="contact-item contact-item--green contact-item--gap">
          <svg class="contact-icon" viewBox="0 0 12 12" aria-hidden="true"><rect width="12" height="12" fill="var(--brand-blue)"/><path d="M4 2.5h2v2H5v3h1v2H4C3 8.5 3 3.5 4 2.5z" fill="#fff"/></svg>
          +41 76 519 84 60
        </li>
        <li class="contact-item">
          <svg class="contact-icon" viewBox="0 0 12 12" aria-hidden="true"><rect width="12" height="12" fill="var(--brand-blue)"/><rect x="2.2" y="3.2" width="7.6" height="5.6" fill="none" stroke="#fff" stroke-width="1"/><path d="M2.2 3.2 6 6.3l3.8-3.1" fill="none" stroke="#fff" stroke-width="1"/></svg>
          info@varnok-fs.ch
        </li>
        <li class="contact-item">
          <svg class="contact-icon" viewBox="0 0 12 12" aria-hidden="true"><rect width="12" height="12" fill="var(--brand-green)"/><path d="M6 2.3 9.5 5.5H8.6v4H6.8V7.2H5.2v2.3H3.4v-4H2.5z" fill="#fff"/></svg>
          www.varnok-fs.ch
        </li>
      </ul>
    </div>
  </section>

</main>
</body>
</html>
```